WEBSITE NEEDED FOR MY COMPANY CALLED BRAVERIDGE HOCKEY DEVELOPMENT

LOOKING FOR A WEBSITE TO MARKET AND SEEL MY HOCKEY DEVELOPMENT PROGRAMS.
NEEDS TO HAVE 5+ PAGES

Target Market(s)

YOUTH SPORTS

Industry/Entity Type

YOUTH ATHLETE DEVELOPMENT

Number of Pages Required

5+ page

Font styles to use
Sans Serif

Colors
0054AA
0677BA
7BADD7
CADEEF
E8F1F8

Requirements
Must have
• MAIN PAGE - SPIRNG PROGRAM PAGE - SUMMER PROGRAM PAGE - WINTER PAGE - TOURNAMENT PAGE
Nice to have
• FLASH
Should not have
• NOT SURE

```html
<!DOCTYPE html>
<html lang="en">
<head>
<meta charset="utf-8">
<title>Summer Program – Braveridge Hockey Development</title>
<link href="https://fonts.googleapis.com/css2?family=Roboto:wght@300;400;500;700&family=Roboto+Condensed:wght@300;400;700&display=swap" rel="stylesheet">
<style>
:root{
  --blue-deep:#0054AA;
  --blue:#0677BA;
  --blue-soft:#7BADD7;
  --blue-pale:#CADEEF;
  --blue-mist:#E8F1F8;
  --navy:#1f3142;
  --navy-dark:#172330;
  --ink:#222;
  --grey-text:#666;
  --card-bg:#f6f6f6;
  --white:#fff;
}
*{box-sizing:border-box;margin:0;padding:0}
html,body{width:1200px;height:2498px;overflow:hidden}
body{position:relative;background:var(--white);font-family:"Roboto",Arial,sans-serif;color:var(--ink)}
.site-header{position:absolute;left:0;top:0;width:1200px;height:78px;z-index:3}
.brand-block{position:absolute;left:0;top:0;width:268px;height:94px;background:var(--navy);clip-path:polygon(0 0,100% 0,86% 100%,0 100%);display:flex;align-items:center;padding-left:30px}
.brand-name{font-family:"Roboto Condensed",sans-serif;font-weight:700;font-size:17px;line-height:19px;color:#3ab7e8;letter-spacing:.5px;width:180px}
.main-nav{position:absolute;left:411px;top:34px;display:flex;gap:0}
.main-nav a{font-size:11.5px;color:#222;text-decoration:none;margin-right:34px;letter-spacing:.2px}
.main-nav a.active{color:var(--blue)}
.social-top{position:absolute;left:923px;top:34px;display:flex;gap:18px}
.social-top span{width:12px;height:12px;border:1.5px solid #444;border-radius:50%}
.contact-btn{position:absolute;left:1032px;top:20px;width:130px;height:38px;border:2px solid var(--blue-deep);color:var(--blue-deep);font-size:11.5px;font-weight:500;display:flex;align-items:center;justify-content:center;text-decoration:none}
.hero{position:absolute;left:0;top:78px;width:1200px;height:392px;background:linear-gradient(100deg,#5d6a3c 0%,#4f6a2c 30%,#8c8a6e 55%,#6f7b45 80%,#3f5a22 100%)}
.hero-title{position:absolute;left:125px;top:205px;font-family:"Roboto Condensed",sans-serif;font-weight:700;font-size:56px;color:var(--white);z-index:2}
.hero-text{position:absolute;left:125px;top:281px;width:400px;font-size:14px;line-height:25px;color:var(--white);z-index:2}
.info-band{position:absolute;left:361px;top:406px;width:839px;height:126px;background:var(--blue);clip-path:polygon(82px 0,100% 0,100% 100%,0 100%);color:var(--white);font-family:"Roboto Condensed",sans-serif}
.band-season{position:absolute;left:121px;top:24px;font-size:32px;font-weight:700}
.band-count{position:absolute;left:121px;top:64px;font-size:28px;font-weight:300}
.band-icon{position:absolute;left:412px;top:36px}
.band-details{position:absolute;left:478px;top:26px;font-size:26px;font-weight:700}
.band-call{position:absolute;left:478px;top:63px;font-size:26px;font-weight:700}
.band-call span{border-bottom:2px solid var(--white);margin-left:8px}
.intro{position:absolute;left:0;top:588px;width:1200px;text-align:center;font-size:25px;line-height:40px;color:#444}
.programs{position:absolute;left:125px;top:719px;display:grid;grid-template-columns:repeat(3,286px);column-gap:46px;row-gap:43px}
.program-card{position:relative;height:407px;background:var(--card-bg)}
.card-photo{height:199px;background:linear-gradient(135deg,#e9eef2 0%,#c9cdd2 45%,#d98a4e 70%,#eef1f4 100%)}
.card-photo.alt{background:linear-gradient(135deg,#eef1f4 0%,#bfc6cd 50%,#e7eaed 100%)}
.day-tag{position:absolute;right:0;top:0;width:121px;height:37px;background:var(--blue-deep);clip-path:polygon(0 0,100% 0,100% 100%,22px 100%);color:var(--white);font-size:12px;display:flex;align-items:center;justify-content:center;padding-left:16px}
.card-head{position:absolute;left:19px;right:23px;top:219px;display:flex;justify-content:space-between;font-family:"Roboto Condensed",sans-serif;font-weight:700;font-size:17.5px}
.card-price{color:var(--blue)}
.card-desc{position:absolute;left:19px;top:253px;width:240px;font-size:13px;line-height:24px;color:var(--grey-text)}
.card-dates{position:absolute;left:19px;top:340px;font-size:11.5px;line-height:24px;color:#444}
.card-dates b{color:#222;font-weight:500}
.more-link{position:absolute;right:23px;top:366px;font-size:12.5px;font-weight:500;color:var(--blue);text-decoration:none}
.site-footer{position:absolute;left:0;top:2133px;width:1200px;height:315px;background:var(--navy);color:var(--white)}
.footer-contact{position:absolute;right:716px;top:94px;text-align:right}
.footer-contact h3,.footer-about h3{font-family:"Roboto Condensed",sans-serif;font-size:17px;font-weight:700;margin-bottom:14px}
.contact-line{display:flex;justify-content:flex-end;align-items:center;gap:12px;font-size:12px;height:24px}
.footer-badge{position:absolute;left:541px;top:61px;width:120px;height:120px;border:3px solid #2ea3dc;border-radius:50%;display:flex;align-items:center;justify-content:center;text-align:center;font-family:"Roboto",sans-serif;font-size:11px;font-weight:700;line-height:14px;color:#2ea3dc;padding:14px}
.footer-about{position:absolute;left:716px;top:94px;width:220px}
.footer-about p{font-size:12px;line-height:19px;color:#e6e9ec}
.footer-social{position:absolute;left:519px;top:232px;display:flex;gap:16px}
.footer-social span{width:28px;height:28px;border:1px solid #cfd6dc;border-radius:50%}
.copyright{position:absolute;left:0;top:2448px;width:1200px;height:50px;background:var(--navy-dark);color:#e6e9ec;font-size:12px;display:flex;align-items:center;justify-content:center}
</style>
</head>
<body>
<header class="site-header">
  <div class="brand-block"><div class="brand-name">BRAVERIDGE HOCKEY DEVELOPMENT</div></div>
  <nav class="main-nav">
    <a href="#">HOME</a><a href="#" class="active">OUR PROGRAM</a><a href="#">TOURNAMENT</a><a href="#">NEWS &amp; EVENTS</a><a href="#">ABOUT US</a>
  </nav>
  <div class="social-top"><span></span><span></span><span></span></div>
  <a href="#" class="contact-btn">CONTACT US</a>
</header>

<section class="hero" role="img" aria-label="Two players competing in a field hockey match on grass"></section>
<h1 class="hero-title">Summer Program</h1>
<p class="hero-text">Lorem ipsum dolor sit amet, consectetur adipiscing eiusmod tempor incididunt ut labore et dolore magna aliqua.</p>

<div class="info-band">
  <div class="band-season">Jul - Aug</div>
  <div class="band-count">Include 09 Programs</div>
  <svg class="band-icon" width="52" height="56" viewBox="0 0 52 56" fill="none" stroke="#fff" stroke-width="2">
    <path d="M44 2 L22 44"/><path d="M22 44 Q18 52 8 50 L4 48"/><ellipse cx="38" cy="48" rx="8" ry="4"/>
  </svg>
  <div class="band-details">For More Details About Program</div>
  <div class="band-call">Call Now<span>+12 345 67890</span></div>
</div>

<p class="intro">Registration is now open for Summer 2022 Skill Development<br>classes at Braveridge Hockey Development</p>

<main class="programs">
  <article class="program-card"><div class="card-photo" role="img" aria-label="Ice hockey face-off with players in orange jerseys"></div><div class="day-tag">MONDAY</div><div class="card-head"><span>Class Name Here</span><span class="card-price">$300.00</span></div><p class="card-desc">Lorem ipsum dolor sit amet, consectetur adipiscing elit, sed do eiusmod tempor incididunt ut labore et dolore magna...</p><div class="card-dates"><b>Start date:</b> 22-05-2022<br><b>End date:</b> 22-08-2022</div><a href="#" class="more-link">MORE DETAIL</a></article>
  <article class="program-card"><div class="card-photo alt" role="img" aria-label="Young hockey player in a white helmet on the bench"></div><div class="day-tag">TUESDAY</div><div class="card-head"><span>Class Name Here</span><span class="card-price">$400.00</span></div><p class="card-desc">Lorem ipsum dolor sit amet, consectetur adipiscing elit, sed do eiusmod tempor incididunt ut labore et dolore magna...</p><div class="card-dates"><b>Start date:</b> 22-05-2022<br><b>End date:</b> 22-08-2022</div><a href="#" class="more-link">MORE DETAIL</a></article>
  <article class="program-card"><div class="card-photo" role="img" aria-label="Referee dropping the puck between two hockey players"></div><div class="day-tag">FRIDAY</div><div class="card-head"><span>Class Name Here</span><span class="card-price">$200.00</span></div><p class="card-desc">Lorem ipsum dolor sit amet, consectetur adipiscing elit, sed do eiusmod tempor incididunt ut labore et dolore magna...</p><div class="card-dates"><b>Start date:</b> 22-05-2022<br><b>End date:</b> 22-08-2022</div><a href="#" class="more-link">MORE DETAIL</a></article>
  <article class="program-card"><div class="card-photo alt" role="img" aria-label="Hockey player in a white jersey number 93 on the ice"></div><div class="day-tag">SATURDAY</div><div class="card-head"><span>Class Name Here</span><span class="card-price">$100.00</span></div><p class="card-desc">Lorem ipsum dolor sit amet, consectetur adipiscing elit, sed do eiusmod tempor incididunt ut labore et dolore magna...</p><div class="card-dates"><b>Start date:</b> 22-05-2022<br><b>End date:</b> 22-08-2022</div><a href="#" class="more-link">MORE DETAIL</a></article>
  <article class="program-card"><div class="card-photo alt" role="img" aria-label="Hockey player skating with the puck"></div><div class="day-tag">SUNDAY</div><div class="card-head"><span>Class Name Here</span><span class="card-price">$300.00</span></div><p class="card-desc">Lorem ipsum dolor sit amet, consectetur adipiscing elit, sed do eiusmod tempor incididunt ut labore et dolore magna...</p><div class="card-dates"><b>Start date:</b> 22-05-2022<br><b>End date:</b> 22-08-2022</div><a href="#" class="more-link">MORE DETAIL</a></article>
  <article class="program-card"><div class="card-photo" role="img" aria-label="Ice hockey face-off with players in orange jerseys"></div><div class="day-tag">SUNDAY</div><div class="card-head"><span>Class Name Here</span><span class="card-price">$500.00</span></div><p class="card-desc">Lorem ipsum dolor sit amet, consectetur adipiscing elit, sed do eiusmod tempor incididunt ut labore et dolore magna...</p><div class="card-dates"><b>Start date:</b> 22-05-2022<br><b>End date:</b> 22-08-2022</div><a href="#" class="more-link">MORE DETAIL</a></article>
  <article class="program-card"><div class="card-photo" role="img" aria-label="Referee dropping the puck between two hockey players"></div><div class="day-tag">FRIDAY</div><div class="card-head"><span>Class Name Here</span><span class="card-price">$500.00</span></div><p class="card-desc">Lorem ipsum dolor sit amet, consectetur adipiscing elit, sed do eiusmod tempor incididunt ut labore et dolore magna...</p><div class="card-dates"><b>Start date:</b> 22-05-2022<br><b>End date:</b> 22-08-2022</div><a href="#" class="more-link">MORE DETAIL</a></article>
  <article class="program-card"><div class="card-photo alt" role="img" aria-label="Young skater practising stickhandling on the rink"></div><div class="day-tag">MONDAY</div><div class="card-head"><span>Class Name Here</span><span class="card-price">$600.00</span></div><p class="card-desc">Lorem ipsum dolor sit amet, consectetur adipiscing elit, sed do eiusmod tempor incididunt ut labore et dolore magna...</p><div class="card-dates"><b>Start date:</b> 22-05-2022<br><b>End date:</b> 22-08-2022</div><a href="#" class="more-link">MORE DETAIL</a></article>
  <article class="program-card"><div class="card-photo" role="img" aria-label="Ice hockey face-off with players in orange jerseys"></div><div class="day-tag">SATURDAY</div><div class="card-head"><span>Class Name Here</span><span class="card-price">$300.00</span></div><p class="card-desc">Lorem ipsum dolor sit amet, consectetur adipiscing elit, sed do eiusmod tempor incididunt ut labore et dolore magna...</p><div class="card-dates"><b>Start date:</b> 22-05-2022<br><b>End date:</b> 22-08-2022</div><a href="#" class="more-link">MORE DETAIL</a></article>
</main>

<footer class="site-footer">
  <div class="footer-contact">
    <h3>Contact Now</h3>
    <div class="contact-line">+112 345 6789
      <svg width="10" height="10" viewBox="0 0 10 10" fill="#fff"><path d="M2 0 L4 2.5 L3 4 Q4.5 6 6 7 L7.5 6 L10 8 L8.5 10 Q4 9.5 0 2 Z"/></svg></div>
    <div class="contact-line">info@example.com
      <svg width="11" height="9" viewBox="0 0 11 9" fill="#fff"><rect width="11" height="9" rx="1"/><path d="M0.5 1 L5.5 5 L10.5 1" stroke="#1f3142" fill="none"/></svg></div>
    <div class="contact-line">253 Main Street, Lorem
      <svg width="9" height="11" viewBox="0 0 9 11" fill="#fff"><path d="M4.5 11 L1 5.5 A4 4 0 1 1 8 5.5 Z"/><circle cx="4.5" cy="4" r="1.5" fill="#1f3142"/></svg></div>
  </div>
  <div class="footer-badge">BRAVERIDGE HOCKEY DEVELOPMENT</div>
  <div class="footer-about">
    <h3>About US</h3>
    <p>Lorem ipsum dolor sit amet, consecte adipiscing elit, sed do eiusmod tempor incididunt ut labore sed do eiusmod incididunt ut labore....</p>
  </div>
  <div class="footer-social"><span></span><span></span><span></span><span></span></div>
</footer>
<div class="copyright">2022 All rights reserved</div>
</body>
</html>
```